Website Redesign Project

Bright Harbor Planning provides project management and project controls consultancy services to companies in many industry sectors, within Australia and overseas. My company has been developing a business brand through forging strong business relationships within industry. We provide innovative tools, concepts and solutions to management teams to assist them in better plan and managing there project portfolios.
SECTORS OF INDUSTRY WE SERVICE
★Oil & Gas
★Minerals & Metals
★Petrochemical
★Manufacturing
★Building & Construction
★Telecommunications
★Rail
★Civil
OLD WEBSITE
My old website www.brightharborplanning.com.au needs a complete overhaul in terms of how the web pages look and feel. I am trying to get away from the grey, washed out look as it is uninviting and dull. My clients commented that my webpage does not reflect who I am as a company or my core values. Think total redesign
DESIGN
I would like a webpage design that is modern and has a corporate image. It must be elegant, classy, and have an overall glossy appearance. I want something exciting that creates some excellent feedback from clients. It needs to have a savvy appearance and an attitude of a market leader. A generic website template cannot be used as I provide a unique service to clients. I do not need a website design that looks like my compeditors, I want something that stands out in the crowd and effectivly markets my bussinesses brand. I want my website to represent quality, so only high resolution images that are clear, sharp and in focus can be used. With this design, throw your standard webpage design concepts out the window, as I want something fresh, innovative, exciting and inviting. The overall design should appear uncluttered as all content needs to be there for a reason, so think functional.
It must be professional and of the highest calibre as my clients expect nothing less. I provide clients with innovative tools, concepts and solutions, so the design needs to be edgy and creative to align with my company’s core business services. The new design must promote the company’s brand and us as a market leader. It must communicate that we service many industry sectors and reflect our company’s creativity, vision, energy and drive.
WEBPAGE WRITTEN CONTENT
I am happy with the written content on each page within my old website. You may arrange the text how you see fit within the new design. On the main page of my old website the text is under scored, I am not a big fan of this. I currently do not like the format the text is in, I am looking for a formatt that is easy to read, looks flattering and pleasing to the eye.
MAIN PAGE DESIGN
The main page design needs to focus on my company as a brand, it must promote that I service many industry sectors. My old webpage had me pigeon holed as only providing services to oil and gas. This is incorrect as I service oil & gas, metals and minerals, Petrochemical, Manufacturing, Building & Construction, Telecommunications, Rail and civil.
WEBPAGE COLUR PREFERENCE
Prefer a white background with plenty of colour
TESTIMONIAL TAB
The testimonial tab on the task bar can be removed as it is no longer required.
FINISHED PRODUCT
The finished product will be uploaded by you to a nominated web hosting account. I will need a copy of all files associated with the design. A copy of the finished product will also be provided in formats that can me imported to Xara Pro Designer as I will update my website in 6 months or so using this tool.
Updates
I have updated the design brief after recieving feedback from several designers
Thanks
Reason: Some designers have asked for more time
Hi All
I have just launched another project called "bright harbor planning business card redesign project", you are all welcome to join this project.
Thanks
Target Market(s)
★Oil and Gas
★Mining and Resources
★Building and infrastructure
★Petrochemical
★Civil and roads
★Rail
Industry/Entity Type
Industry
Requirements
Must have
- ★Draw you in
★Hold your attention
★Identify company brand
★Highlight skills experience and expertise
★Be a unique design not generic
Should not have
- ★The webpage design should not be old fashioned
★ The design should not be based off a generic design template
★The webpage should not be cluttered; everything needs to be there for a reason.

```html
<!DOCTYPE html>
<html lang="en">
<head>
<meta charset="utf-8">
<title>Bright Harbor Planning</title>
<link href="https://fonts.googleapis.com/css2?family=Roboto+Condensed:wght@400;700&family=Roboto:wght@300;400&display=swap" rel="stylesheet">
<style>
:root{
  --red:#e91c24;
  --red-soft:#f47f84;
  --ink:#1a1a1a;
  --nav:#565656;
  --nav-line:#6c6c6c;
  --text:#6f6f6f;
  --icon:#7a7a7a;
  --rule:#c9d3d6;
  --footer:#454441;
  --footer-line:#8a8985;
  --base:#111;
  --white:#fff;
}
*{margin:0;padding:0;box-sizing:border-box}
html,body{width:791px;height:1200px;overflow:hidden;background:var(--white)}
body{position:relative;font-family:"Roboto",Arial,sans-serif;font-weight:300;color:var(--text)}
.abs{position:absolute}
.cond{font-family:"Roboto Condensed","Arial Narrow",sans-serif}

.top-line{left:0;top:0;width:791px;height:2px;background:var(--red)}

/* header */
.brand{left:68px;top:26px;display:flex;align-items:center;gap:8px}
.brand-mark{width:26px;height:26px;background:var(--red)}
.brand-name{font-family:"Roboto Condensed",sans-serif;font-weight:700;font-size:23px;color:var(--ink);letter-spacing:.2px;line-height:1}
.brand-tag{left:102px;top:57px;font-size:7.6px;font-weight:400;color:var(--ink)}
.contact{right:93px;font-family:"Roboto Condensed",sans-serif;font-weight:700;font-size:9px;color:#444;display:flex;align-items:center;gap:4px}
.contact svg{width:12px;height:12px}

/* nav */
.nav{left:0;top:88px;width:791px;height:33px;background:var(--nav);border-top:1px solid #777}
.nav ul{list-style:none;display:flex;position:absolute;left:74px;top:0;height:33px}
.nav li{height:33px;line-height:33px;font-family:"Roboto Condensed",sans-serif;font-weight:700;font-size:9.5px;color:var(--white);text-transform:uppercase;text-align:center;border-right:1px solid var(--nav-line)}
.nav li.active{background:var(--red);border-top:3px solid #c8141b;line-height:28px}

/* hero */
.hero{left:0;top:121px;width:791px;height:274px;background:var(--red)}
.hero-title{left:84px;top:156px;color:var(--white);font-family:"Roboto Condensed",sans-serif;font-weight:700;line-height:1}
.hero-title .l1{font-size:23px;display:block}
.hero-title .l2{font-size:33px;display:block;margin-top:2px}
.hero-copy{left:84px;top:236px;width:142px;font-size:7.4px;line-height:12px;color:var(--white);text-align:justify;font-weight:400}
.hero-frame{left:282px;top:135px;width:428px;height:283px;background:var(--red-soft);border-radius:5px}
.hero-photo{left:286px;top:139px;width:420px;height:276px;border-radius:4px;
  background:linear-gradient(180deg,#3a2a10 0%,#b8781c 30%,#f2c04a 42%,#9a5a12 60%,#2a1a08 100%)}
.hero-shadow{left:316px;top:418px;width:360px;height:8px;border-radius:50%;background:radial-gradient(ellipse,rgba(0,0,0,.18),transparent 70%)}
.dots{left:425px;top:398px;width:141px;height:35px;background:var(--red);display:flex;justify-content:center;align-items:center;gap:10px}
.dot{width:15px;height:15px;border:1.4px solid var(--white);border-radius:50%;color:var(--white);font-size:7px;font-weight:700;font-family:"Roboto Condensed",sans-serif;display:flex;align-items:center;justify-content:center}
.dot.on{background:var(--white);color:var(--red)}

/* more button */
.more{width:57px;height:21px;background:var(--white);border-left:6px solid var(--ink);font-family:"Roboto Condensed",sans-serif;font-weight:700;font-size:10px;color:var(--red);display:flex;align-items:center;justify-content:center}
.more::after{content:"";position:absolute;right:4px;bottom:-4px;border-left:4px solid transparent;border-right:4px solid transparent;border-top:4px solid var(--white)}
.more.red{background:var(--red);color:var(--white)}
.more.red::after{border-top-color:var(--red)}

/* sectors */
.sector-line{left:0;top:487px;width:791px;height:1px;background:var(--rule)}
.sector{width:150px;text-align:center;top:461px}
.sector svg{display:block;margin:0 auto}
.sector h3{font-family:"Roboto Condensed",sans-serif;font-weight:700;font-size:15px;color:var(--red);margin-top:20px}
.sector p{font-size:7.6px;line-height:12px;margin-top:4px;letter-spacing:.2px}
.stem{width:1px;height:28px;background:var(--rule);margin:0 auto}

.section-rule{left:74px;top:670px;width:643px;height:1px;background:var(--red)}

.heading{font-family:"Roboto Condensed",sans-serif;font-weight:700;font-size:17px;color:var(--red);text-transform:uppercase;letter-spacing:-.1px}
.body-copy{font-size:7.6px;line-height:12px;text-align:justify;letter-spacing:.1px}

/* knowledge */
.k-item{left:374px;width:347px;height:68px}
.k-hex{position:absolute;left:0;top:0;width:62px;height:66px}
.k-title{position:absolute;left:69px;top:4px;font-family:"Roboto Condensed",sans-serif;font-weight:700;font-size:12px;color:var(--red)}
.k-text{position:absolute;left:70px;top:21px;width:272px;font-size:7.4px;line-height:12px}
.k-box{position:absolute;left:62px;top:40px;width:285px;height:18px;border-right:1px solid #ddd;border-bottom:1px solid #ddd}

/* social */
.social{left:349px;top:1019px;display:flex;gap:4px;z-index:2}
.social span{width:15px;height:15px;border-radius:2px;background:#dfe3e8;border:1px solid #b9c0c8}

.band{left:0;top:1029px;width:791px;height:31px;background:var(--red)}
.footer{left:0;top:1060px;width:791px;height:113px;background:var(--footer)}
.f-col{top:1071px;width:93px}
.f-col svg{width:11px;height:11px}
.f-col .f-rule{height:1px;background:var(--footer-line);margin:4px 0 8px}
.f-col a{display:block;color:#e8e8e8;font-size:8px;text-decoration:none;line-height:16.5px;letter-spacing:.3px}
.f-col.info{width:150px}
.f-col.info p{color:var(--white);font-size:7.8px;line-height:10px;letter-spacing:.3px}
.base{left:0;top:1173px;width:791px;height:27px;background:var(--base);color:#8b8b8b;font-size:7.6px;text-align:center;line-height:27px;letter-spacing:.2px}
</style>
</head>
<body>
<div class="abs top-line"></div>

<header>
  <div class="abs brand"><span class="brand-mark"></span><span class="brand-name">BRIGHT HARBOR PLANNING</span></div>
  <div class="abs brand-tag">Providing Effective Project Controls and Management Solutions</div>
  <div class="abs contact" style="top:34px">Ph: + 61 0400 555 128
    <svg viewBox="0 0 12 12"><path d="M3 1 L5 3 L4 5 Q5 7 7 8 L9 7 L11 9 L9 11 Q3 10 1 3 Z" fill="#e91c24"/></svg></div>
  <div class="abs contact" style="top:56px">Email: daniel@brightharborplanning.com.au
    <svg viewBox="0 0 12 12"><circle cx="6" cy="6" r="5.5" fill="#e91c24"/><circle cx="6" cy="6" r="2" fill="none" stroke="#fff" stroke-width="1.2"/><path d="M8 4 V7 Q8 8.5 9.5 7.5" fill="none" stroke="#fff" stroke-width="1.1"/></svg></div>
</header>

<nav class="abs nav">
  <ul>
    <li class="active" style="width:59px">About Us</li>
    <li style="width:69px">Expertise</li>
    <li style="width:80px">Knowledge</li>
    <li style="width:78px">Experience</li>
    <li style="width:66px">Projects</li>
    <li style="width:62px">Focus</li>
    <li style="width:59px">Contact</li>
    <li style="width:79px">Testimonials</li>
    <li style="width:92px;border-right:none">Recruitment</li>
  </ul>
</nav>

<section>
  <div class="abs hero"></div>
  <h1 class="abs hero-title"><span class="l1">Bright Harbor</span><span class="l2">Planning</span></h1>
  <p class="abs hero-copy">I provide services to companies in the mining and oil and gas sector to enabling them to plan and manage their construction projects more effectively. This is achieved by evaluating the businesses practices and them implementing different tools and solutions.</p>
  <div class="abs more" style="left:85px;top:341px">more</div>
  <div class="abs hero-frame"></div>
  <div class="abs hero-photo" role="img" aria-label="Offshore oil platforms silhouetted against a golden sunset sky over the sea"></div>
  <div class="abs hero-shadow"></div>
  <div class="abs dots"><span class="dot">1</span><span class="dot">2</span><span class="dot on">3</span><span class="dot">4</span><span class="dot">5</span></div>
</section>

<section>
  <div class="abs sector-line"></div>
  <div class="abs sector" style="left:61px">
    <svg width="52" height="52" viewBox="0 0 52 52"><circle cx="26" cy="26" r="26" fill="#7a7a7a"/><g fill="#fff"><rect x="16" y="22" width="20" height="4"/><rect x="18" y="26" width="2" height="12"/><rect x="32" y="26" width="2" height="12"/><rect x="24" y="26" width="4" height="12"/><rect x="20" y="12" width="3" height="10"/><rect x="28" y="16" width="6" height="6"/></g></svg>
    <div class="stem"></div><h3>Oil &amp; Gas</h3>
    <p>Oil &amp; Gas Solutions provides project management and project controls consultancy services to companies in many industry sectors, within Australia and overseas.</p>
  </div>
  <div class="abs sector" style="left:234px">
    <svg width="52" height="52" viewBox="0 0 52 52"><circle cx="26" cy="26" r="25" fill="none" stroke="#7a7a7a" stroke-width="8" stroke-dasharray="9 4"/><circle cx="26" cy="26" r="15" fill="#fff"/><rect x="18" y="22" width="16" height="8" fill="#333"/><rect x="22" y="18" width="8" height="5" fill="#333"/></svg>
    <div class="stem"></div><h3>Metals &amp; Minerals</h3>
    <p>Metal &amp; Minerals Solutions provides project management and project controls consultancy services to companies in many industry sectors, within Australia and overseas.</p>
  </div>
  <div class="abs sector" style="left:404px">
    <svg width="52" height="52" viewBox="0 0 52 52"><g fill="none" stroke="#7a7a7a" stroke-width="3"><path d="M14 26 A12 12 0 0 1 38 26"/><path d="M8 28 A18 18 0 0 1 44 28"/><path d="M3 30 A23 23 0 0 1 49 30"/></g><path d="M26 20 L18 46 H21 L26 32 L31 46 H34 Z" fill="#222"/><circle cx="26" cy="20" r="3" fill="#222"/></svg>
    <div class="stem"></div><h3>Telecommunications</h3>
    <p>Telecommunication Solutions provides project management and project controls consultancy services to companies in many industry sectors, within Australia and overseas.</p>
  </div>
  <div class="abs sector" style="left:579px">
    <svg width="52" height="52" viewBox="0 0 52 52"><circle cx="26" cy="26" r="26" fill="#7a7a7a"/><rect x="15" y="12" width="22" height="24" rx="4" fill="#fff"/><rect x="18" y="16" width="16" height="8" fill="#7a7a7a"/><circle cx="20" cy="30" r="2" fill="#7a7a7a"/><circle cx="32" cy="30" r="2" fill="#7a7a7a"/><path d="M17 36 L14 42 M35 36 L38 42" stroke="#fff" stroke-width="2"/></svg>
    <div class="stem"></div><h3>Rail &amp; Civil</h3>
    <p>Rail &amp; Civil Solutions provides project management and project controls consultancy services to companies in many industry sectors, within Australia and overseas.</p>
  </div>
</section>

<div class="abs section-rule"></div>

<section>
  <h2 class="abs heading" style="left:75px;top:693px">Welcome to Bright Harbor Planning</h2>
  <p class="abs body-copy" style="left:75px;top:729px;width:274px">I provide services to companies in the mining and oil and gas sector to enabling them to plan and manage their construction projects more effectively. This is achieved by evaluating the businesses practices and them implementing different tools and solutions.<br>My clients are then able to plan and deliver their projects, on time and within their budgets. I am able to provide services to both large and small scale businesses within Australian and Overseas. I offer my clients value</p>
  <div class="abs more red" style="left:75px;top:824px">more</div>
  <h2 class="abs heading" style="left:75px;top:861px">Project Management Systems</h2>
  <p class="abs body-copy" style="left:75px;top:886px;width:274px">To deliver a successful project effective planning and managing of resources is important. On various projects in Australia and Overseas I have designed and implemented project controls management systems for medium to large scale projects. I also developed preconfigured project controls templates that can be customised to suit any project.</p>
  <div class="abs more red" style="left:75px;top:964px">more</div>
</section>

<section>
  <h2 class="abs heading" style="left:377px;top:693px">Knowledge</h2>
  <div class="abs k-item" style="top:730px">
    <div class="k-box"></div>
    <svg class="k-hex" viewBox="0 0 62 66" role="img" aria-label="Illustration of a rocket launching for project management"><polygon points="31,0 62,16 62,50 31,66 0,50 0,16" fill="#e3e6ea"/></svg>
    <div class="k-title">Project Management</div>
    <p class="k-text">I have a wide range of project management, governance and assurance experience that can be used to deliver a successful project. My experience and understanding of the full life cycle of a project enables</p>
  </div>
  <div class="abs k-item" style="top:805px">
    <div class="k-box"></div>
    <svg class="k-hex" viewBox="0 0 62 66" role="img" aria-label="Illustration of a red and white toy figure for management style"><polygon points="31,0 62,16 62,50 31,66 0,50 0,16" fill="#e8e2de"/></svg>
    <div class="k-title" style="top:5px">Management Style</div>
    <p class="k-text">Strong communication skills, approachability and an excellent work ethic allow me to work efficiently within any work environment. I have an easy going management approach,</p>
  </div>
  <div class="abs k-item" style="top:879px">
    <div class="k-box"></div>
    <svg class="k-hex" viewBox="0 0 62 66" role="img" aria-label="Illustration of a cartoon bird on a yellow background for project constructability"><polygon points="31,0 62,16 62,50 31,66 0,50 0,16" fill="#f6d27a"/></svg>
    <div class="k-title">Project Constructability</div>
    <p class="k-text">All good managers aspire to create an environment where construction can commence in a safe, logical, realistic and practical manner. I can provide assistance to develop a construction method</p>
  </div>
  <div class="abs more red" style="left:381px;top:964px">more</div>
</section>

<div class="abs social" aria-label="Social links"><span></span><span></span><span></span><span></span><span></span></div>
<div class="abs band"></div>

<footer>
  <div class="abs footer"></div>
  <div class="abs f-col" style="left:83px">
    <svg viewBox="0 0 12 12"><path d="M1 2 H11 V8 H5 L2 11 V8 H1 Z" fill="#ddd"/></svg>
    <div class="f-rule"></div>
    <a>Home</a><a>About us</a><a>Expertise</a><a>Reporting</a>
  </div>
  <div class="abs f-col" style="left:243px">
    <svg viewBox="0 0 12 12"><path d="M1 5 H3 V11 H1 Z M4 5 L6 1 Q7.5 1 7 4 H10.5 Q11.5 4.5 11 6 L10 10.5 H4 Z" fill="none" stroke="#ddd"/></svg>
    <div class="f-rule"></div>
    <a>Projects</a><a>Focus</a><a>Testimonial</a><a>News &amp; Events</a>
  </div>
  <div class="abs f-col" style="left:426px">
    <svg viewBox="0 0 12 12"><path d="M2 1 H8 L10 3 V11 H2 Z M4 5 H8 M4 7 H8 M4 9 H8" fill="none" stroke="#ddd"/></svg>
    <div class="f-rule"></div>
    <a>Terms &amp; Condition</a><a>Recruitment</a><a>Contact us</a>
  </div>
  <div class="abs f-col info" style="left:602px">
    <svg viewBox="0 0 12 12"><rect x="1" y="2.5" width="10" height="7.5" fill="#ddd"/><path d="M1 2.5 L6 7 L11 2.5" fill="none" stroke="#454441"/></svg>
    <div class="f-rule" style="width:93px"></div>
    <p>Daniel Ashford<br>Tel: 0400555128<br>daniel@brightharbor<br>planning.com.au<br>www.brightharborplanning.com.au</p>
  </div>
  <div class="abs base">© COPYRIGHT BY 2013 BRIGHT HARBOR PLANNING. ALL RIGHTS RESERVED</div>
</footer>
</body>
</html>
```